Billboard Design for Harbor Lane Dentistry

Brookhaven Family Dental Care
Phone number: 318-562-0913
Address: 248 Castleford Blvd
Hours: 7am-5pm ; Monday-Friday

Dental Implant Surgery
Same Day Emergency Visits
Cosmetic Treatments
GLINT! Whitening

NAMES: Dr. Colin Varnstaad
Dr. Peter Ashdale

MOST INSURANCES ACCEPTED

Eye catching slogan/colors/design for billboard

Our website is www.brookhavenfamilydentalcare.example to see current branding.

Target Market(s)

Target market is anyone in Alexandria. Focus on Families and High End Cosmetic Dentistry.

Industry/Entity Type

Dental Clinic

Requirements
Must have
• Brookhaven Family Dental Care
• Phone number: 318-562-0913
• Address: 248 Castleford Blvd
• Hours: 7am-5pm ; Monday-Friday
• Dental Implant Surgery
• Same Day Emergency Visits
• Cosmetic Treatments
• GLINT! Whitening
• NAMES: Dr. Colin Varnstaad
• Dr. Peter Ashdale
• and logo
Nice to have
• digital billboard-try to catch attention with color or phrase
Should not have
• Can not make claims or compare to other area dentist's according to laws.

```html
<!DOCTYPE html>
<html lang="en">
<head>
<meta charset="utf-8">
<title>Brookhaven Family Dental Care Billboard</title>
<link href="https://fonts.googleapis.com/css2?family=Lexend:wght@500;600;700&display=swap" rel="stylesheet">
<style>
  :root {
    --navy: #0f3670;
    --navy-text: #1b3264;
    --brick: #8e3230;
    --white: #ffffff;
    --teal: #3fb4c9;
    --rule: #c9ccd3;
    --sky-light: #f3ede6;
    --sky-warm: #e9cfb6;
    --shade: #5b4a3e;
  }
  * { margin: 0; padding: 0; box-sizing: border-box; }
  html, body {
    width: 1200px; height: 571px; overflow: hidden;
    background: var(--white);
    font-family: "Lexend", "Helvetica Neue", Arial, sans-serif;
  }
  .billboard {
    position: relative; width: 1200px; height: 571px; overflow: hidden;
    background: var(--white);
  }
  .title-band {
    position: absolute; left: 0; top: 0; width: 1200px; height: 93px;
    background: var(--navy);
    display: flex; align-items: center; justify-content: center;
  }
  .title-band h1 {
    color: var(--white); font-weight: 700; font-size: 55px;
    letter-spacing: 0.5px; text-transform: uppercase; line-height: 1;
  }
  .hero {
    position: absolute; left: 0; top: 93px; width: 1200px; height: 383px;
  }
  .hero-photo {
    position: absolute; left: 0; top: 0; width: 620px; height: 383px;
    background:
      radial-gradient(ellipse at 40% 75%, var(--shade) 0%, rgba(91,74,62,0.55) 35%, rgba(91,74,62,0) 70%),
      linear-gradient(180deg, var(--sky-light) 0%, var(--sky-warm) 100%);
  }
  .hero-panel { position: absolute; left: 0; top: 0; }
  .services { list-style: none; position: absolute; left: 0; top: 0; width: 1200px; height: 383px; }
  .services li {
    position: absolute; color: var(--white); font-weight: 600;
    font-size: 36px; line-height: 1; white-space: nowrap;
  }
  .services li::before { content: "• "; }
  .footer {
    position: absolute; left: 0; top: 476px; width: 1200px; height: 95px;
    background: var(--white);
  }
  .brand-mark {
    position: absolute; left: 140px; top: 18px; width: 166px; height: 62px;
    display: flex; align-items: center; gap: 8px;
  }
  .brand-mark .mark-square { width: 18px; height: 18px; background: var(--teal); flex: none; }
  .brand-mark .mark-name {
    color: var(--teal); font-weight: 600; font-size: 13px; line-height: 1.2;
    text-transform: uppercase; letter-spacing: 0.5px;
  }
  .footer-rule {
    position: absolute; left: 309px; top: 10px; width: 1px; height: 74px; background: var(--rule);
  }
  .doctors {
    position: absolute; left: 324px; top: 8px;
    color: var(--navy-text); font-weight: 600; font-size: 32px; line-height: 1.2; white-space: nowrap;
  }
  .contact {
    position: absolute; left: 324px; top: 55px;
    color: var(--navy-text); font-weight: 600; font-size: 18px; line-height: 1.2; white-space: nowrap;
  }
</style>
</head>
<body>
<main class="billboard">
  <header class="title-band">
    <h1>Brookhaven Family Dental Care</h1>
  </header>

  <section class="hero">
    <div class="hero-photo" role="img" aria-label="Photo of four smiling friends in sunglasses embracing outdoors against a bright sky"></div>
    <svg class="hero-panel" width="1200" height="383" viewBox="0 0 1200 383" aria-hidden="true">
      <polygon points="604,0 1200,0 1200,383 520,383" fill="var(--brick)"/>
    </svg>
    <ul class="services">
      <li style="left:638px; top:22px;">Cosmetic Treatments</li>
      <li style="left:618px; top:92px;">GLINT! Whitening</li>
      <li style="left:600px; top:164px;">Same Day Emergency Visits</li>
      <li style="left:582px; top:236px;">Dental Implant Surgery</li>
      <li style="left:562px; top:308px;">Most insurances accepted</li>
    </ul>
  </section>

  <footer class="footer">
    <div class="brand-mark">
      <span class="mark-square"></span>
      <span class="mark-name">Brookhaven Family Dental Care</span>
    </div>
    <div class="footer-rule"></div>
    <p class="doctors">Dr. Colin Varnstaad &amp; Dr. Peter Ashdale</p>
    <p class="contact">248 Castleford Blvd | 7am - 5pm; Monday - Friday | P: (318) 562-0913</p>
  </footer>
</main>
</body>
</html>
```